Mailchimp email (Monthly performance report design)

We need someone to code an HTML file as this will be used to import the template to Mailchimp.

We need a slick and professionally designed email layout to be used via Mailchimp. The target audience is sophisticated investors.

We have attached our current email template that is being used (File name: Capture 1). We have also added an inspiration piece (File name: Capture). The content needs to be transferred to the new template. We have 3 funds and we want them to be somehow presented in 3 columns. The pictures need to be professional business or nature bleu theme. We have also uploaded a template to provide you with guidance on how the layout should be. You are free to use your imagination and make changes as deemed.

This is our website: https://www.tesmarobridge.com/. The color theme of the template should match the website.

The pictures need to be professional business or nature bleu theme.

```html
<!DOCTYPE html>
<html lang="en">
<head>
<meta charset="utf-8">
<title>Tesmaro Bridge – Monthly Report</title>
<link rel="stylesheet" href="https://fonts.googleapis.com/css2?family=Montserrat:wght@400;500;700;800;900&display=swap">
<style>
  :root {
    --navy: #1f3a57;
    --ice: #eef6fd;
    --ink: #0d0d0d;
    --white: #ffffff;
    --lime: #a6e85c;
    --grey-bar: #c2c2c2;
    --photo-a: #9fb3c2;
    --photo-b: #e6ecef;
  }
  * { box-sizing: border-box; margin: 0; padding: 0; }
  html, body { width: 1200px; height: 2762px; overflow: hidden; }
  body {
    position: relative;
    background: var(--white);
    font-family: "Montserrat", Arial, sans-serif;
    color: var(--ink);
  }
  .block { position: absolute; left: 0; width: 1200px; }

  /* Header */
  .site-header { top: 0; height: 144px; background: var(--white); }
  .brand { position: absolute; display: flex; align-items: center; gap: 18px; }
  .brand-mark { width: 92px; height: 92px; border-radius: 50%; background: var(--ink); flex: none; }
  .brand-name { font-weight: 500; font-size: 40px; letter-spacing: 4px; color: var(--ink); white-space: nowrap; }
  .site-header .brand { left: 44px; top: 26px; }
  .main-nav { position: absolute; right: 44px; top: 56px; display: flex; gap: 44px; }
  .main-nav a { font-size: 30px; font-weight: 500; color: var(--ink); text-decoration: none; letter-spacing: .5px; }

  /* Hero */
  .hero { top: 144px; height: 550px; }
  .hero-photo { position: absolute; inset: 0; background: linear-gradient(120deg, #cfd7dc 0%, #7fa6c4 35%, #c7d2d8 70%, #e9ecee 100%); }
  .hero-panel {
    position: absolute; left: 688px; top: 0; width: 452px; height: 550px;
    background: var(--navy); display: flex; align-items: center; padding-left: 52px;
  }
  .hero-title { color: var(--white); font-weight: 900; font-size: 62px; line-height: 1.06; letter-spacing: 1px; }

  /* Funds */
  .funds { top: 694px; height: 624px; background: var(--ice); }
  .fund { position: absolute; top: 92px; width: 340px; text-align: center; }
  .fund-photo { width: 312px; height: 312px; margin: 0 auto; border-radius: 50%; border: 3px solid var(--navy); }
  .fund-name { margin-top: 36px; font-weight: 700; font-size: 32px; line-height: 38px; letter-spacing: .5px; }
  .fund--opportunities { left: 60px; }
  .fund--opportunities .fund-photo { background: linear-gradient(140deg, #e9e4e2, #c99a9a 55%, #5a5f68); }
  .fund--canada { left: 432px; }
  .fund--canada .fund-photo { background: linear-gradient(140deg, #d8302c 0%, #efe7e2 45%, #c9a98a 100%); }
  .fund--us { left: 804px; }
  .fund--us .fund-photo { background: linear-gradient(160deg, #3c4c86 0%, #1c2a55 50%, #1f6b3e 100%); }

  /* About */
  .about { top: 1318px; height: 816px; background: var(--white); }
  .about-photo {
    position: absolute; left: 44px; top: 158px; width: 432px; height: 518px;
    border: 2px solid #d0d6da;
    background: radial-gradient(circle at 50% 60%, #d9c6a0 0%, #a8c98a 45%, #d8ead0 100%);
  }
  .about-item { position: absolute; left: 520px; width: 640px; }
  .about-item--about { top: 162px; }
  .about-item--mission { top: 460px; }
  .about-head { display: flex; align-items: center; gap: 18px; }
  .about-icon { width: 96px; height: 96px; flex: none; }
  .about-title { font-weight: 800; font-size: 44px; letter-spacing: .5px; }
  .about-text { margin-top: 14px; font-size: 28px; line-height: 38px; width: 600px; }
  .divider { position: absolute; left: 520px; top: 420px; width: 680px; height: 3px; background: var(--lime); }

  /* Footer */
  .site-footer { top: 2134px; height: 534px; }
  .footer-brand-area { position: absolute; left: 0; top: 0; width: 578px; height: 534px; background: var(--ice); }
  .footer-brand-area .brand { left: 44px; top: 224px; }
  .footer-contact { position: absolute; left: 578px; top: 0; width: 622px; height: 534px; background: var(--navy); color: var(--white); }
  .address { position: absolute; left: 58px; font-weight: 700; font-size: 28px; line-height: 38px; }
  .address--street { top: 86px; }
  .address--city { top: 200px; }
  .contact-box {
    position: absolute; left: 42px; height: 58px; border: 2px solid var(--white);
    padding: 0 14px; display: flex; align-items: center;
    font-weight: 700; font-size: 28px; white-space: nowrap;
  }
  .contact-box--phone { top: 298px; }
  .contact-box--tollfree { top: 362px; }
  .contact-box--email { top: 428px; }

  .copyright {
    top: 2668px; height: 94px; background: var(--grey-bar);
    display: flex; align-items: center; justify-content: center;
    font-size: 28px; font-weight: 500;
  }
</style>
</head>
<body>

<header class="block site-header">
  <div class="brand">
    <span class="brand-mark"></span>
    <span class="brand-name">TESMARO BRIDGE</span>
  </div>
  <nav class="main-nav">
    <a href="https://www.tesmarobridge.com/">ABOUT</a>
    <a href="https://www.tesmarobridge.com/">FUND</a>
    <a href="https://www.tesmarobridge.com/">CONTACT</a>
  </nav>
</header>

<section class="block hero">
  <div class="hero-photo" role="img" aria-label="Laptop on a desk displaying financial line charts"></div>
  <div class="hero-panel">
    <h1 class="hero-title">MONTHLY<br>REPORT</h1>
  </div>
</section>

<section class="block funds">
  <div class="fund fund--opportunities">
    <div class="fund-photo" role="img" aria-label="Laptop screen showing a funding page"></div>
    <h2 class="fund-name">OPPORTUNITIES<br>FUND</h2>
  </div>
  <div class="fund fund--canada">
    <div class="fund-photo" role="img" aria-label="Canadian flag with hundred dollar bank notes"></div>
    <h2 class="fund-name">CANADIAN SMALL<br>CAP FUND</h2>
  </div>
  <div class="fund fund--us">
    <div class="fund-photo" role="img" aria-label="American flag with stock market candlestick chart"></div>
    <h2 class="fund-name">US SMALL<br>CAP FUND</h2>
  </div>
</section>

<section class="block about">
  <div class="about-photo" role="img" aria-label="Hand holding a glass jar of coins with a young plant growing from it"></div>

  <div class="about-item about-item--about">
    <div class="about-head">
      <svg class="about-icon" viewBox="0 0 96 96" aria-hidden="true">
        <circle cx="48" cy="48" r="45" fill="var(--white)" stroke="var(--lime)" stroke-width="3"/>
        <rect x="34" y="30" width="28" height="38" rx="6" fill="#6f7f52"/>
        <circle cx="48" cy="50" r="8" fill="#e8c24a"/>
      </svg>
      <h3 class="about-title">ABOUT TESMARO BRIDGE</h3>
    </div>
    <p class="about-text">Lorem Ipsum is simply dummy text of the printing and typesetting industry. Lorem Ipsum has been the industry</p>
  </div>

  <div class="divider"></div>

  <div class="about-item about-item--mission">
    <div class="about-head">
      <svg class="about-icon" viewBox="0 0 96 96" aria-hidden="true">
        <circle cx="48" cy="48" r="45" fill="var(--white)" stroke="var(--lime)" stroke-width="3"/>
        <rect x="28" y="52" width="8" height="16" fill="#3b4a6b"/>
        <rect x="40" y="46" width="8" height="22" fill="#e8a33a"/>
        <rect x="52" y="40" width="8" height="28" fill="#3b4a6b"/>
        <rect x="64" y="34" width="8" height="34" fill="#d9463a"/>
        <polyline points="28,44 44,36 56,32 70,24" fill="none" stroke="#d9463a" stroke-width="3"/>
      </svg>
      <h3 class="about-title">OUR MISSION</h3>
    </div>
    <p class="about-text">Lorem Ipsum is simply dummy text of the printing and typesetting industry. Lorem Ipsum has been the industry</p>
  </div>
</section>

<footer class="block site-footer">
  <div class="footer-brand-area">
    <div class="brand">
      <span class="brand-mark"></span>
      <span class="brand-name">TESMARO BRIDGE</span>
    </div>
  </div>
  <div class="footer-contact">
    <p class="address address--street">2480 HARCOURT AVENUE WEST,<br>SUITE 1170</p>
    <p class="address address--city">MONTREAL (QC), CANADA<br>H2X 4T9</p>
    <div class="contact-box contact-box--phone">PHONE: +1 (514) 555-0187</div>
    <div class="contact-box contact-box--tollfree">TOLL FREE: +1 (844) 555-0143</div>
    <div class="contact-box contact-box--email">INFO@TESMAROBRIDGE.COM</div>
  </div>
</footer>

<div class="block copyright">©2022 by Tesmaro Bridge Capital Management Inc.</div>

</body>
</html>
```